Author needs a new book, Kindle and Audiobook cover design

I updated and re-edited a book I wrote 25 years ago but now realize the title and design did not get the job done. I am seeking a book, Kindle and audiobook design that will make me stand out. The final design will pop while being sensitive to the nature of the subject. The title of the book is Quiet Lanterns. Subtitle: Ways to Notice and Step Away From Harmful Circles While Keeping Steady Belief by Dorian T. Wexcombe. I am wanting to get the attention of people who have been damaged by a church relationship that started well but ended badly.
Updates

The book title is: Quiet Lanterns. The Subtitle is: Ways To Notice and Step Away From Harmful Circles While Keeping Steady Belief. The dimension is 6x9 (150 pages) and I am the author: Dorian T. Wexcombe

Target Market(s)

People with a church experience; church leadership. Religious abuse victims.

Industry/Entity Type

Christian

Font styles to use
Serif

Colors

Designer to choose colors to be used in the design.

Requirements
Nice to have
• I am not married to the Serif font if another design works better.

```html
<!DOCTYPE html>
<html lang="en">
<head>
<meta charset="utf-8">
<title>Quiet Lanterns — Book Cover</title>
<link href="https://fonts.googleapis.com/css2?family=Cinzel:wght@400;500&family=Montserrat:wght@500&display=swap" rel="stylesheet">
<style>
  :root {
    --page-bg: #d9dde2;
    --stone-light: #a57a52;
    --stone-mid: #7a5234;
    --stone-dark: #3f2616;
    --arch-rim: #b08960;
    --night: #050403;
    --gold-light: #f1cf8c;
    --gold: #c99a52;
    --gold-deep: #8f6428;
    --cream: #efe6d6;
  }
  html, body {
    margin: 0;
    padding: 0;
    width: 1179px;
    height: 1200px;
    overflow: hidden;
    background: var(--page-bg);
  }
  .book-cover {
    position: absolute;
    left: 209px;
    top: 41px;
    width: 760px;
    height: 1117px;
    overflow: hidden;
    background: var(--night);
    box-shadow: 0 10px 30px rgba(0,0,0,0.25);
  }
  .cover-art {
    position: absolute;
    inset: 0;
    width: 100%;
    height: 100%;
  }
  .cover-text {
    position: absolute;
    left: 0;
    right: 0;
    text-align: center;
  }
  .author-name {
    top: 740px;
    font-family: "Montserrat", sans-serif;
    font-weight: 500;
    font-size: 22px;
    letter-spacing: 1.5px;
    color: var(--cream);
    text-transform: uppercase;
  }
  .book-title {
    top: 790px;
    margin: 0;
    font-family: "Cinzel", serif;
    font-weight: 400;
    line-height: 0.98;
    text-transform: uppercase;
    background: linear-gradient(180deg, var(--gold-light) 0%, var(--gold) 55%, var(--gold-deep) 100%);
    -webkit-background-clip: text;
    background-clip: text;
    color: transparent;
  }
  .book-title .title-line-small { display: block; font-size: 84px; letter-spacing: 2px; }
  .book-title .title-line-large { display: block; font-size: 96px; letter-spacing: 1px; }
  .book-subtitle {
    top: 1000px;
    left: 130px;
    right: 130px;
    margin: 0;
    font-family: "Montserrat", sans-serif;
    font-weight: 500;
    font-size: 17px;
    line-height: 1.45;
    letter-spacing: 0.3px;
    color: var(--cream);
    text-transform: uppercase;
  }
</style>
</head>
<body>
  <main class="book-cover">
    <svg class="cover-art" viewBox="0 0 760 1117" xmlns="http://www.w3.org/2000/svg">
      <defs>
        <linearGradient id="stoneWall" x1="0" y1="0" x2="1" y2="1">
          <stop offset="0" stop-color="var(--stone-mid)"/>
          <stop offset="0.45" stop-color="var(--stone-light)"/>
          <stop offset="1" stop-color="var(--stone-dark)"/>
        </linearGradient>
        <linearGradient id="fadeToNight" x1="0" y1="0" x2="0" y2="1">
          <stop offset="0.45" stop-color="var(--night)" stop-opacity="0"/>
          <stop offset="0.78" stop-color="var(--night)" stop-opacity="1"/>
        </linearGradient>
        <linearGradient id="archInterior" x1="0" y1="0" x2="0" y2="1">
          <stop offset="0" stop-color="#1c1410"/>
          <stop offset="0.5" stop-color="#0b0807"/>
          <stop offset="1" stop-color="var(--night)"/>
        </linearGradient>
      </defs>
      <rect class="stone-wall" width="760" height="1117" fill="url(#stoneWall)" role="img" aria-label="Weathered sandstone church wall"/>
      <path class="arch-rim" d="M70 1117 L70 560 Q70 330 380 120 Q690 330 690 560 L690 1117 Z" fill="none" stroke="var(--arch-rim)" stroke-width="46" opacity="0.55"/>
      <path class="arch-window" d="M136 1117 L136 580 Q136 390 380 235 Q624 390 624 580 L624 1117 Z" fill="url(#archInterior)" role="img" aria-label="Dark gothic archway with a stern clergyman gripping iron bars"/>
      <rect class="night-fade" width="760" height="1117" fill="url(#fadeToNight)"/>
    </svg>

    <div class="cover-text author-name">Dorian T. Wexcombe</div>
    <h1 class="cover-text book-title">
      <span class="title-line-small">Quiet</span>
      <span class="title-line-large">Lanterns</span>
    </h1>
    <p class="cover-text book-subtitle">Ways To Notice and Step Away From Harmful Circles While Keeping Steady Belief</p>
  </main>
</body>
</html>
```